Rate sheet redesign

We provide rate sheets to agents for our scenic flights and I would like to make them easier to read and more comprehensive. I'd also like to be able to edit the information in the design, as tours get updated and so do the rates. We've got new product out of shark bay, so the sections would need to be: Perth, Geraldton, Kalbarri and Shark Bay. I've attached what we've been using and also some concept photos.

also a link to our flights online: https://coralwingtours.bookvista.com/catalog/418752/flights-from-perth

I've put this under brochure redesign as I wasn't sure what a rate sheet would be considered. Open to different formats if it means content is editable.

Need extra days to review

```html
<!DOCTYPE html>
<html lang="en">
<head>
<meta charset="utf-8">
<title>Coralwing Aviation – Rate Retail 25/26</title>
<link rel="stylesheet" href="https://fonts.googleapis.com/css2?family=Montserrat:wght@500;600;700;800;900&family=Open+Sans:wght@400;600;700&display=swap">
<style>
  :root {
    --stage: #dcdcdc;
    --paper: #ffffff;
    --blue: #2f6db5;
    --navy: #1f3c8c;
    --sky: #5aa6e2;
    --sky-deep: #3d86d0;
    --orange: #f0a030;
    --orange-line: #f2b55a;
    --ink-soft: #6d86b3;
    --sun: #f1d391;
    --gold: #e5b867;
    --haze: #a9bdd2;
  }
  * { box-sizing: border-box; margin: 0; padding: 0; }
  html, body { width: 1200px; height: 3000px; overflow: hidden; }
  body {
    background: var(--stage);
    font-family: "Open Sans", Arial, sans-serif;
    display: flex;
    flex-direction: column;
    align-items: center;
    justify-content: space-evenly;
  }

  .page {
    background: var(--paper);
    position: relative;
    overflow: hidden;
    box-shadow: 0 10px 24px rgba(0,0,0,.12);
  }
  .spread {
    display: flex;
    width: 1100px;
    height: 387px;
    box-shadow: 0 12px 28px rgba(0,0,0,.14);
  }
  .spread .page { width: 550px; height: 387px; box-shadow: none; }
  .spread .page:first-child::after {
    content: "";
    position: absolute; top: 0; right: 0; bottom: 0; width: 26px;
    background: linear-gradient(to right, rgba(0,0,0,0), rgba(0,0,0,.08));
  }
  .spread .page:last-child::before {
    content: "";
    position: absolute; top: 0; left: 0; bottom: 0; width: 18px;
    background: linear-gradient(to left, rgba(0,0,0,0), rgba(0,0,0,.06));
  }

  /* brand lockup */
  .brand {
    display: flex; align-items: center; gap: 7px;
    font-family: "Montserrat", Arial, sans-serif;
    font-weight: 700; color: var(--blue);
  }
  .brand-dot { border-radius: 50%; background: var(--orange); flex: none; }

  /* skyline photo area */
  .skyline {
    position: absolute; left: 0; right: 0; bottom: 0;
    background: linear-gradient(to bottom,
      rgba(255,255,255,1) 0%, var(--sun) 30%, var(--gold) 55%, var(--haze) 80%, #7f9bbd 100%);
  }

  /* front cover */
  .cover { width: 700px; height: 493px; }
  .cover .brand { position: absolute; top: 46px; left: 50%; transform: translateX(-50%); font-size: 17px; }
  .cover .brand-dot { width: 14px; height: 14px; }
  .cover-title {
    position: absolute; top: 92px; width: 100%; text-align: center;
    font-family: "Montserrat", Arial, sans-serif; font-weight: 900;
    font-size: 62px; letter-spacing: 1px; color: var(--blue);
  }
  .cover-regions {
    position: absolute; top: 180px; left: 50%; transform: translateX(-50%);
    border: 1.5px solid var(--orange-line);
    padding: 8px 26px;
    font-family: "Montserrat", Arial, sans-serif; font-weight: 800;
    font-size: 15px; letter-spacing: .5px; white-space: nowrap;
    color: var(--blue);
  }
  .cover-regions .accent { color: var(--orange); }
  .cover .skyline { height: 260px; }

  /* back cover */
  .back .brand { position: absolute; top: 70px; left: 50%; transform: translateX(-50%); font-size: 16px; }
  .back .brand-dot { width: 13px; height: 13px; }
  .contact-list {
    position: absolute; top: 112px; left: 50%; transform: translateX(-50%);
    list-style: none; display: flex; flex-direction: column; gap: 6px;
    font-size: 11px; font-weight: 600; color: var(--navy);
  }
  .contact-list li { display: flex; align-items: center; gap: 7px; }
  .contact-list svg { width: 11px; height: 11px; flex: none; }
  .spread .skyline { height: 190px; }

  .front-small .brand { position: absolute; top: 40px; left: 50%; transform: translateX(-50%); font-size: 13px; }
  .front-small .brand-dot { width: 11px; height: 11px; }
  .front-small .cover-title { top: 66px; font-size: 44px; }
  .front-small .cover-regions { top: 130px; font-size: 11px; padding: 6px 18px; }

  /* contents page */
  .contents-frame {
    position: absolute; top: 36px; left: 44px; right: 44px; bottom: 40px;
    border: 2px solid var(--navy);
  }
  .contents-label {
    position: absolute; left: 18px; bottom: 60px;
    transform: rotate(-90deg); transform-origin: left top;
    font-family: "Montserrat", Arial, sans-serif; font-weight: 900;
    font-size: 17px; color: var(--navy); white-space: nowrap;
    background: var(--paper); padding: 0 6px;
  }
  .contents-label .accent { color: var(--orange); }
  .contents-table {
    position: absolute; top: 22px; left: 36px; right: 20px;
    border-collapse: collapse; width: calc(100% - 56px);
    font-size: 9px; color: #fff;
  }
  .contents-table th {
    background: var(--orange); font-family: "Montserrat", Arial, sans-serif;
    font-weight: 800; font-size: 11px; letter-spacing: .5px;
    padding: 8px; text-align: center; border: 1px solid #fff;
  }
  .contents-table td { padding: 17px 8px; text-align: center; border: 1px solid rgba(255,255,255,.5); }
  .contents-table .cell-location { background: var(--navy); font-weight: 700; }
  .contents-table .cell-address { background: var(--sky-deep); }
  .contents-table .cell-pages { background: var(--sky); font-weight: 700; }

  /* rate pages */
  .rate-page { padding: 34px 30px 0 34px; }
  .rate-page .brand { position: absolute; top: 14px; right: 24px; font-size: 9px; }
  .rate-page .brand-dot { width: 8px; height: 8px; }
  .rate-title {
    font-family: "Montserrat", Arial, sans-serif; font-weight: 900;
    font-size: 21px; color: var(--navy); letter-spacing: .3px;
  }
  .rate-title .accent { color: var(--orange); }
  .rate-subtitle { font-size: 8px; color: var(--ink-soft); margin: 2px 0 10px; }
  .rate-table { width: 100%; border-collapse: collapse; table-layout: fixed; }
  .rate-table th, .rate-table td {
    border: 1px solid var(--orange-line);
    text-align: left; vertical-align: top; padding: 6px 7px;
  }
  .rate-table th {
    font-family: "Montserrat", Arial, sans-serif; font-weight: 800;
    font-size: 10px; color: var(--navy);
  }
  .rate-table th small { display: block; font-family: "Open Sans", Arial, sans-serif; font-weight: 400; font-size: 7px; color: var(--ink-soft); }
  .rate-table td { font-size: 8px; line-height: 1.45; color: var(--ink-soft); height: 64px; }
  .rate-table td.flight { color: var(--navy); font-weight: 600; }
  .rate-table td.price { color: var(--navy); font-weight: 700; font-size: 10px; }
  .rate-table tr > :first-child { border-left: none; }
  .rate-table tr > :last-child { border-right: none; }
  .rate-table thead th { border-top: none; }
  .rate-note {
    position: absolute; left: 34px; right: 30px; bottom: 26px;
    display: flex; align-items: center; gap: 9px;
    font-size: 7.5px; font-weight: 700; text-transform: uppercase; color: var(--navy);
  }
  .rate-note::before { content: ""; width: 14px; height: 14px; background: var(--orange); flex: none; }
</style>
</head>
<body>

  <!-- front cover -->
  <section class="page cover">
    <div class="brand"><span class="brand-dot"></span>Coralwing Aviation</div>
    <h1 class="cover-title">RATE RETAIL</h1>
    <p class="cover-regions">PERTH , GERALDTON , <span class="accent">KALBARRI , SHARK BAY</span></p>
    <div class="skyline" role="img" aria-label="Photograph of a city skyline at sunrise"></div>
  </section>

  <!-- outer covers -->
  <section class="spread">
    <div class="page back">
      <div class="brand"><span class="brand-dot"></span>Coralwing Aviation</div>
      <ul class="contact-list">
        <li><svg viewBox="0 0 12 12"><path d="M2.5 1h2l1 3-1.3 1a6 6 0 0 0 2.8 2.8l1-1.3 3 1v2A1 1 0 0 1 10 11 9 9 0 0 1 1 2a1 1 0 0 1 1.5-1z" fill="var(--orange)"/></svg>08 5550 0142</li>
        <li><svg viewBox="0 0 12 12"><rect x="1" y="2.5" width="10" height="7" rx="1" fill="var(--orange)"/><path d="M1.5 3l4.5 3.5L10.5 3" stroke="#fff" fill="none"/></svg>info@coralwingaviation.au</li>
        <li><svg viewBox="0 0 12 12"><circle cx="6" cy="6" r="5" fill="var(--orange)"/><path d="M1 6h10M6 1c-2.5 3-2.5 7 0 10M6 1c2.5 3 2.5 7 0 10" stroke="#fff" stroke-width=".8" fill="none"/></svg>www.coralwingaviation.com.au</li>
      </ul>
      <div class="skyline" role="img" aria-label="Photograph of a city skyline at sunrise"></div>
    </div>
    <div class="page front-small">
      <div class="brand"><span class="brand-dot"></span>Coralwing Aviation</div>
      <h2 class="cover-title">RATE RETAIL</h2>
      <p class="cover-regions">PERTH , GERALDTON , <span class="accent">KALBARRI , SHARK BAY</span></p>
      <div class="skyline" role="img" aria-label="Photograph of a city skyline at sunrise"></div>
    </div>
  </section>

  <!-- contents + Geraldton -->
  <section class="spread">
    <div class="page">
      <div class="contents-frame">
        <table class="contents-table">
          <thead><tr><th>LOCATION</th><th>ADDRESS</th><th>PAGES</th></tr></thead>
          <tbody>
            <tr><td class="cell-location">Perth</td><td class="cell-address">Hangar 4, Airport Drive</td><td class="cell-pages">03</td></tr>
            <tr><td class="cell-location">Geraldton</td><td class="cell-address">Terminal Road, Geraldton</td><td class="cell-pages">04</td></tr>
            <tr><td class="cell-location">Kalbarri</td><td class="cell-address">Kalbarri Airstrip, Ajana Road</td><td class="cell-pages">06</td></tr>
            <tr><td class="cell-location">Shark Bay</td><td class="cell-address">Airport Road, Denham</td><td class="cell-pages">08</td></tr>
          </tbody>
        </table>
      </div>
      <p class="contents-label"><span class="accent">25/26</span> RATES RETAIL</p>
    </div>
    <div class="page rate-page">
      <div class="brand"><span class="brand-dot"></span>Coralwing</div>
      <h2 class="rate-title">GERALDTON <span class="accent">RATES</span></h2>
      <p class="rate-subtitle">Scenic flights departing Geraldton airport daily</p>
      <table class="rate-table">
        <thead><tr><th>Flight</th><th>Inclusions</th><th>Classes</th><th>Adult<small>per person</small></th><th>Child<small>per person</small></th></tr></thead>
        <tbody>
          <tr><td class="flight">Abrolhos Islands Scenic</td><td>Return flight, island commentary</td><td>Daily 9am</td><td class="price">$395</td><td class="price">$295</td></tr>
          <tr><td class="flight">Abrolhos Island Landing</td><td>Flight, lunch, snorkel gear</td><td>Mon Wed Fri</td><td class="price">$695</td><td class="price">$520</td></tr>
          <tr><td class="flight">Geraldton Coast Flight</td><td>Coastline and city views</td><td>Daily 2pm</td><td class="price">$250</td><td class="price">$190</td></tr>
        </tbody>
      </table>
      <p class="rate-note">Please note prices include GST and are subject to change without notice.</p>
    </div>
  </section>

  <!-- Geraldton spread -->
  <section class="spread">
    <div class="page rate-page">
      <div class="brand"><span class="brand-dot"></span>Coralwing</div>
      <h2 class="rate-title">GERALDTON <span class="accent">RATES</span></h2>
      <p class="rate-subtitle">Scenic flights departing Geraldton airport daily</p>
      <table class="rate-table">
        <thead><tr><th>Flight</th><th>Inclusions</th><th>Classes</th><th>Adult<small>per person</small></th><th>Child<small>per person</small></th></tr></thead>
        <tbody>
          <tr><td class="flight">Abrolhos Islands Scenic</td><td>Return flight, island commentary</td><td>Daily 9am</td><td class="price">$395</td><td class="price">$295</td></tr>
          <tr><td class="flight">Abrolhos Island Landing</td><td>Flight, lunch, snorkel gear</td><td>Mon Wed Fri</td><td class="price">$695</td><td class="price">$520</td></tr>
          <tr><td class="flight">Geraldton Coast Flight</td><td>Coastline and city views</td><td>Daily 2pm</td><td class="price">$250</td><td class="price">$190</td></tr>
        </tbody>
      </table>
      <p class="rate-note">Please note prices include GST and are subject to change without notice.</p>
    </div>
    <div class="page rate-page">
      <div class="brand"><span class="brand-dot"></span>Coralwing</div>
      <h2 class="rate-title">GERALDTON <span class="accent">RATES</span></h2>
      <p class="rate-subtitle">Scenic flights departing Geraldton airport daily</p>
      <table class="rate-table">
        <thead><tr><th>Flight</th><th>Inclusions</th><th>Classes</th><th>Adult<small>per person</small></th><th>Child<small>per person</small></th></tr></thead>
        <tbody>
          <tr><td class="flight">Abrolhos Islands Scenic</td><td>Return flight, island commentary</td><td>Daily 9am</td><td class="price">$395</td><td class="price">$295</td></tr>
          <tr><td class="flight">Abrolhos Island Landing</td><td>Flight, lunch, snorkel gear</td><td>Mon Wed Fri</td><td class="price">$695</td><td class="price">$520</td></tr>
          <tr><td class="flight">Geraldton Coast Flight</td><td>Coastline and city views</td><td>Daily 2pm</td><td class="price">$250</td><td class="price">$190</td></tr>
        </tbody>
      </table>
      <p class="rate-note">Please note prices include GST and are subject to change without notice.</p>
    </div>
  </section>

  <!-- Geraldton + Geraldton–Kalbarri spread -->
  <section class="spread">
    <div class="page rate-page">
      <div class="brand"><span class="brand-dot"></span>Coralwing</div>
      <h2 class="rate-title">GERALDTON <span class="accent">RATES</span></h2>
      <p class="rate-subtitle">Scenic flights departing Geraldton airport daily</p>
      <table class="rate-table">
        <thead><tr><th>Flight</th><th>Inclusions</th><th>Classes</th><th>Adult<small>per person</small></th><th>Child<small>per person</small></th></tr></thead>
        <tbody>
          <tr><td class="flight">Abrolhos Islands Scenic</td><td>Return flight, island commentary</td><td>Daily 9am</td><td class="price">$395</td><td class="price">$295</td></tr>
          <tr><td class="flight">Abrolhos Island Landing</td><td>Flight, lunch, snorkel gear</td><td>Mon Wed Fri</td><td class="price">$695</td><td class="price">$520</td></tr>
          <tr><td class="flight">Geraldton Coast Flight</td><td>Coastline and city views</td><td>Daily 2pm</td><td class="price">$250</td><td class="price">$190</td></tr>
        </tbody>
      </table>
      <p class="rate-note">Please note prices include GST and are subject to change without notice.</p>
    </div>
    <div class="page rate-page">
      <div class="brand"><span class="brand-dot"></span>Coralwing</div>
      <h2 class="rate-title">GERALDTON - <span class="accent">KALBARRI RATES</span></h2>
      <p class="rate-subtitle">Scenic flights departing Kalbarri airstrip daily</p>
      <table class="rate-table">
        <thead><tr><th>Flight</th><th>Inclusions</th><th>Classes</th><th>Adult<small>per person</small></th><th>Child<small>per person</small></th></tr></thead>
        <tbody>
          <tr><td class="flight">Murchison Gorge Flight</td><td>Flight over river gorges</td><td>Daily 10am</td><td class="price">$310</td><td class="price">$230</td></tr>
          <tr><td class="flight">Kalbarri Coast Landing</td><td>Flight, transfer, cliff walk</td><td>Tue Thu Sat</td><td class="price">$560</td><td class="price">$420</td></tr>
          <tr><td class="flight">Pink Lake Loop</td><td>Lake and coastline views</td><td>Daily 3pm</td><td class="price">$280</td><td class="price">$210</td></tr>
        </tbody>
      </table>
      <p class="rate-note">Please note prices include GST and are subject to change without notice.</p>
    </div>
  </section>

</body>
</html>
```